브랜드 소개
[한빛만화회관]
1995년 5월 개관한 '한빛만화회관'는 한국 콘텐츠산업 진흥의 구심점으로 만화, 애니메이션 산업을 종합적으로 지원하고 집중 육성하기 위하여 서울특별시에서 설립하고 도시기업지원단(KDM)가 운영하고 있습니다.
Check 1. 한빛만화회관가 재건축 됩니다. 재건축 기간동안 인근(회현사거리)에 대체 운영공간 조성 및 시민서비스를 제공합니다.
Check 2. 1층 책그림방 : 책그림방은 국내외 만화책은 물론 애니메이션관련 도서자료, 정기간행물 및 학술자료 등을 체계적으로 수집 소장하고 있는 국내 최대규모의 트랜디한 만화서적 문화공간 입니다.
Check 3. 2층 캐릭나들이 : 국내를 대표하는 '캐릭터와 함께 떠나는 서울여행'이라는 컨셉으로 '꼬미루, 부릉, 하늘날개단, 아기너구리, 변신로보카, 다온별이, 느림곰돌 등 콘텐츠 체험문화공간 입니다.

```html
<!DOCTYPE html>
<html lang="ko">
<head>
<meta charset="utf-8">
<title>Dorimak Comics — Business Cards</title>
<link rel="stylesheet" href="https://fonts.googleapis.com/css2?family=Montserrat:wght@500;800&display=swap">
<style>
  :root {
    --backdrop: #e9e7e1;
    --card-red: #e8665a;
    --card-white: #f7f6f2;
    --card-paper: #fbfbf9;
    --ink: #2a2a2a;
    --pattern-teal: #2fb59a;
    --pattern-coral: #ea5a4e;
    --pattern-yellow: #ece3a6;
  }
  html, body {
    margin: 0;
    padding: 0;
    width: 1198px;
    height: 1200px;
    overflow: hidden;
    background: var(--backdrop);
    font-family: "Montserrat", Arial, sans-serif;
  }
  .card-sheet {
    position: relative;
    width: 1198px;
    height: 1200px;
  }
  .card {
    position: absolute;
    width: 520px;
    height: 316px;
    box-shadow: 0 10px 28px rgba(0, 0, 0, 0.12);
    box-sizing: border-box;
  }
  .card--front-red { left: 50px; top: 190px; background: var(--card-red); }
  .card--back-pattern { left: 628px; top: 190px; background: var(--card-paper); }
  .card--front-white { left: 339px; top: 640px; background: var(--card-white); }

  .brand {
    position: absolute;
    left: 0;
    right: 0;
    display: flex;
    align-items: center;
    justify-content: center;
    gap: 10px;
    color: var(--ink);
    font-weight: 800;
    letter-spacing: 0.02em;
    text-transform: uppercase;
    white-space: nowrap;
  }
  .brand__mark {
    flex: none;
    width: 12px;
    height: 12px;
    background: var(--ink);
  }
  .card--front-red .brand {
    top: 126px;
    font-size: 22px;
  }
  .card--front-white .brand {
    top: 96px;
    font-size: 26px;
    line-height: 1.05;
  }
  .brand__name--stacked {
    text-align: center;
  }
  .pattern-fill {
    position: absolute;
    inset: 0;
    background:
      radial-gradient(circle at 25% 30%, rgba(47,181,154,0.35), transparent 35%),
      radial-gradient(circle at 75% 70%, rgba(234,90,78,0.3), transparent 35%),
      var(--pattern-yellow);
    opacity: 0.75;
  }
  .contact {
    position: absolute;
    left: 40px;
    bottom: 34px;
    margin: 0;
    color: var(--ink);
    font-size: 11px;
    font-weight: 500;
    line-height: 1.5;
  }
</style>
</head>
<body>
  <main class="card-sheet">
    <section class="card card--front-red">
      <div class="brand"><span class="brand__mark"></span><span class="brand__name">Dorimak Comics</span></div>
    </section>

    <section class="card card--back-pattern">
      <div class="pattern-fill" role="img" aria-label="Repeating pattern of coral and teal house shapes with pale yellow dots"></div>
    </section>

    <section class="card card--front-white">
      <div class="brand"><span class="brand__mark"></span><span class="brand__name brand__name--stacked">Dorimak<br>Comics</span></div>
      <p class="contact">
        +82. 010.0000.1234<br>
        info.@dorimak.example<br>
        dorimakcomics.example
      </p>
    </section>
  </main>
</body>
</html>
```